Plan of Joint Exploration Venture

I need a multi page prospects design. A cover page, table of contents, and content pages. I'm looking for the basic design now for each page, with content to be filled in later. For now, you can use blank content or random content pulled from anywhere. The table of contents will include: Investment Overview, Details of the Offer, Details of the Strategy, and Management Team Bios. Please use the logo and pictures attached; also, I've attached a general example.

```html
<!DOCTYPE html>
<html lang="en">
<head>
<meta charset="utf-8">
<title>Investment Overview – Spread</title>
<link rel="stylesheet" href="https://fonts.googleapis.com/css2?family=Roboto:wght@400;700&family=Questrial&display=swap">
<style>
  :root {
    --paper: #ffffff;
    --ink: #000000;
    --photo: #000000;
  }
  * { margin: 0; padding: 0; box-sizing: border-box; }
  html, body { width: 1200px; height: 848px; overflow: hidden; background: var(--paper); }
  .spread { position: relative; width: 1200px; height: 848px; color: var(--ink); }
  .page { position: absolute; top: 0; width: 600px; height: 848px; }
  .page--left { left: 0; }
  .page--right { left: 600px; }

  .running-head {
    position: absolute; top: 23px;
    font-family: "Roboto", sans-serif; font-size: 12px; letter-spacing: 0.1px;
  }
  .running-head__num, .running-head__title { position: absolute; white-space: nowrap; }
  .page--left .running-head { left: 36px; }
  .page--left .running-head__title { left: 36px; }
  .page--right .running-head { left: 375px; }
  .page--right .running-head__title { left: 45px; }

  .page-title {
    position: absolute; left: 36px; top: 90px;
    font-family: "Roboto", sans-serif; font-weight: 700; font-size: 28.5px;
    letter-spacing: -0.2px; white-space: nowrap;
  }

  .column {
    position: absolute; width: 225px;
    font-family: "Questrial", sans-serif; font-size: 11.6px; line-height: 16px;
    white-space: nowrap;
  }
  .column p + p { margin-top: 16px; }
  .page--left .column--first { left: 36px; top: 174px; }
  .page--left .column--second { left: 265px; top: 174px; }
  .page--right .column--first { left: 31px; top: 378px; }
  .page--right .column--second { left: 260px; top: 378px; }

  .feature-photo {
    position: absolute; left: 31px; top: 81px; width: 523px; height: 285px;
    background: var(--photo);
  }

  .folio {
    position: absolute; top: 803px;
    font-family: "Roboto", sans-serif; font-size: 12px;
  }
  .page--left .folio { left: 36px; }
  .page--right .folio { right: 46px; }
</style>
</head>
<body>
<main class="spread">

  <section class="page page--left">
    <header class="running-head"><span class="running-head__num">01</span><span class="running-head__title">INVESTMENT OVERVIEW</span></header>
    <h1 class="page-title">INVESTMENT OVERVIEW</h1>

    <div class="column column--first">
      <p>Lorem ipsum dolor sit amet,<br>consectetur adipiscing elit. Etiam<br>ac tortor justo. Proin ullamcorper<br>enim eget congue suscipit. Quisque<br>eleifend quis turpis vel congue.<br>Vestibulum ante ipsum primis in<br>faucibus orci luctus et ultrices<br>posuere cubilia Curae; Mauris<br>eleifend eros et est ornare, nec<br>hendrerit arcu accumsan. Integer<br>sed gravida velit, at pulvinar ligula.<br>Nulla egestas, lorem a scelerisque<br>cursus, lectus urna molestie est,<br>quis porttitor nisl libero ut tortor.<br>Pellentesque habitant morbi<br>tristique senectus et netus et<br>malesuada fames ac turpis egestas.<br>Praesent et libero blandit, ultricies<br>dui sit amet, semper orci. Aenean<br>fringilla, erat a imperdiet auctor,<br>augue risus consequat sapien, at<br>dictum justo est quis nunc. Nullam<br>fringilla lacus vel leo accumsan,<br>vitae dignissim sapien aliquet.</p>
      <p>Pellentesque habitant morbi<br>tristique senectus et netus et<br>malesuada fames ac turpis egestas.<br>In elementum eros in eleifend<br>posuere. Morbi rutrum in libero in<br>condimentum. Mauris vitae ex at<br>neque aliquam lacinia id sit amet<br>libero. Vestibulum in metus quis<br>magna iaculis facilisis ac porta<br>nunc. Donec imperdiet orci at</p>
    </div>

    <div class="column column--second">
      <p>porttitor rhoncus. Morbi sagittis<br>laoreet risus. Mauris at leo auctor,<br>placerat nisl et, facilisis quam.<br>Mauris velit quam, facilisis sit amet<br>tempus sed, facilisis sit amet nulla.<br>Sed velit turpis, fermentum vitae<br>diam ut, condimentum congue<br>enim. Maecenas dapibus nunc<br>eget facilisis mattis. Suspendisse<br>neque leo, molestie sit amet ex et,<br>consequat commodo mi. Aliquam<br>vitae tortor viverra, mollis justo<br>et, gravida dolor. Nam maximus<br>rhoncus tellus, quis tristique quam<br>mattis ac. Nulla facilisi.</p>
      <p>Vivamus in sapien dapibus,<br>euismod nisl feugiat, rhoncus ipsum.<br>Sed bibendum rutrum quam, vitae<br>viverra mi feugiat et. Integer ultrices<br>dictum tellus in ultricies. Nulla<br>ultrices arcu vitae mauris ultrices,<br>suscipit aliquam massa semper.<br>Praesent ultrices fermentum augue<br>quis dignissim. Praesent semper leo<br>orci, ut tempus sapien tristique et.<br>Curabitur efficitur imperdiet dolor,<br>vitae cursus diam facilisis sit amet.<br>Phasellus vitae arcu metus. Cras<br>cursus mi at magna elementum,<br>sit amet dapibus est ultrices.<br>Vestibulum elementum dolor nec<br>tellus auctor feugiat. Aenean ut<br>lorem congue, placerat erat ut,<br>lobortis velit. Sed risus ipsum, varius<br>vel lacinia nec, varius eget ipsum.</p>
    </div>

    <div class="folio">6</div>
  </section>

  <section class="page page--right">
    <header class="running-head"><span class="running-head__num">01</span><span class="running-head__title">INVESTMENT OVERVIEW</span></header>

    <div class="feature-photo" role="img" aria-label="Feature photograph for the investment overview"></div>

    <div class="column column--first">
      <p>Pellentesque elementum, diam ac<br>consequat dictum, enim mauris<br>tincidunt ex, a fringilla turpis sem et<br>diam. Donec erat ligula, lacinia sed<br>posuere ac, blandit sed ipsum. Nulla<br>in neque purus.</p>
      <p>Cras sit amet lectus leo. Nullam<br>aliquet, nisi ut consequat dictum,<br>sapien ligula commodo eros, ac<br>imperdiet nibh turpis vel velit.<br>Donec lobortis, sapien ut mattis<br>iaculis, nunc odio faucibus magna,<br>eu vestibulum erat sapien vitae<br>nisi. Donec placerat fringilla nunc,<br>eget maximus dui maximus nec.<br>Integer lacus augue, commodo non<br>metus quis, varius cursus erat. Proin<br>dapibus bibendum odio ut volutpat.<br>Aliquam tortor libero, vulputate at<br>tristique id, molestie eu sem. Duis<br>tempor et magna id lobortis. In sed<br>mauris a turpis gravida interdum</p>
    </div>

    <div class="column column--second">
      <p>vel ac justo. Morbi et finibus velit.<br>Integer venenatis odio at magna<br>ultricies blandit vitae eget enim.<br>Etiam eu enim vel mi rhoncus<br>tristique.</p>
      <p>Suspendisse aliquam augue blandit<br>elit ultrices tempor. Duis molestie,<br>augue et ultricies placerat, massa<br>turpis bibendum ipsum, ac mattis<br>diam dui pharetra ipsum. Praesent<br>nec elit et ante cursus viverra vitae<br>vel neque. Donec pulvinar porta<br>mi quis iaculis. Nam ultricies, lacus<br>in dapibus fermentum, velit quam<br>ultricies velit, eu commodo nulla<br>risus fringilla enim. Nam vel quam<br>sit amet sem ultrices tristique<br>hendrerit id orci. Integer eu rhoncus<br>nisi. Curabitur ut pulvinar urna.<br>Etiam in elit tortor. Morbi lacinia<br>purus eu nibh pulvinar aliquet.<br>Vestibulum lacinia, metus sed</p>
    </div>

    <div class="folio">7</div>
  </section>

</main>
</body>
</html>
```